Etiketten-Design für nachhaltige Rasur- & Pflegeprodukte
Mit Rosalind haben wir einen sehr freundlichen Kontakt, auch im Nachhinein waren noch Anpassungen möglich. Außerdem zeigt sie sich verständnisvoll, von unserer Seite hat sich die Lieferung von Infos manchmal verzögert. Sie dagegen ist schnell wie der Blitz. Das Ergebnis ihrer Arbeit ist außerdem herausragend, wir sind begeistert. Liebe Grüße Jens
> Wir suchen Verpackung und Etiketten für eine Marke für nachhaltige Rasur- & Pflegeprodukte.
Habedere liebe Designer,
„Habedere“ sagt man bei uns in Bayern, es bedeutet Hallo oder auf Wiedersehen, je nach Gelegenheit. In diesem Fall: Hallo.
Vielleicht kennst du uns schon, wir sind tidewinders, wir betreiben einen kleinen Shop für Bartpflege & Rasur unter tidewinders.example und wir versuchen uns nun an einem neuen Thema: nachhaltige Rasur- & Pflegeprodukte für Frauen.
Das machen wir unter dem Namen „Flau“.
Weil die Frage schon oft aufkam: Jawohl, wir haben uns dafür die Beine und die Achseln mit einem Rasierhobel rasiert.
> Zielgruppe.
Wir arbeiten an einer neuen Pflegelinie für Frauen, die sich vorwiegend mit der Rasur und den dazugehörigen Pflegeprodukten beschäftigt. Die Zielgruppe sind vor allem online-affine Frauen aus Deutschland, Österreich und der Schweiz, aber sicher auch europaweit im Alter von 21-45.
> Aufgabenstellung.
Wir sind auf der Suche nach einem Konzept für unsere Produktverpackungen bzw. Etiketten. Bei den Pflegeprodukten verzichten wir bewusst auf eine Umverpackung.
Konkret geplant sind ein Rasierhobel, dafür haben wir eine schöne Umverpackung. Außerdem starten wir mit Rasieröl, Rasierseife und einem After Shave Balsam. Es werden später noch andere Artikel dazukommen, eine Deocreme zum Beispiel.
Rasieröl, Rasiercreme und After Shave Balsam duften nach Orangen, es werden zwei oder drei weitere Duftrichtungen folgen, die eine wird beispielsweise nach Beeren duften, die andere nach Pfirsich und Mango – bitte beachte das bei der Erstellung des Konzeptes, die Unterschiede sollten später auf den ersten Blick erkennbar sein.
Zurück zum Thema Orange: Wir würden den Duft als leicht herben Zitrusduft bezeichnen.
> Die Maße.
• Umverpackung Rasierhobel, weißer Karton (165x90x40mm)
• Rasieröl 30ml (Etikett: 100x46mm)
• Rasiercreme 60ml (Etikett: 156x32mm)
• After Shave Balsam 60ml (Etikett: 156x32mm)
> Zwingend erforderliche Angaben.
Da es sich um Kosmetikprodukte handelt, sind einige Angaben auf dem Label zwingend erforderlich, beispielhaft sollen die folgenden Infos als Platzhalter dienen.
• Hergestellt für Torsten Kählbrink e.K. von tidewinders, Holunderweg 27, 83047 Kolbenried
• Ingredients: Aqua, Stearic Acid, Cocos Nucifera oil, Glycerin, Potassium Hydroxide, Litsea Cubeba oil, (and) Citrus Sinensis Peel oil, Orbignya Oleifera oil, Sodium Hydroxide, Macadamia ternifolia oil, Talc, Kaolin, Citric Acid, Simmondsia chinensis oil, Maris sal, C.I. 77892 (and) Rad Clay, Citral, Limonene, Linalool, Geraniol
• Platz für einen Barcode
• Rasieröl sind 30ml / 1.01 FL.OZ. ODER Creme & Balsam jeweils 60ml / 2.03 FL. OZ.
Wir haben ein Bild der aktuellen Gefäße beigefügt, es kann aber durchaus sein, dass wir uns noch umen..

```html
<!DOCTYPE html>
<html lang="de">
<head>
<meta charset="utf-8">
<title>Flau – Etiketten & Verpackung</title>
<link href="https://fonts.googleapis.com/css2?family=Montserrat:wght@400;500;600;700&display=swap" rel="stylesheet">
<style>
  :root{
    --white:#ffffff;
    --label-white:#f4f4f4;
    --orange:#f0a21e;
    --orange-text:#e3a243;
    --yellow:#fbe08c;
    --teal:#13808c;
    --teal-band:#92cfd1;
    --green:#3f6d61;
    --green-band:#a9d8ce;
    --green-text:#3b5d55;
    --sage:#8db3a8;
    --sage-band:#80b1a3;
    --flap:#4b8a74;
    --line:#1e1e1e;
  }
  *{margin:0;padding:0;box-sizing:border-box}
  html,body{width:1200px;height:848px;overflow:hidden;background:var(--white)}
  body{position:relative;font-family:"Montserrat",sans-serif}
  .label{position:absolute;overflow:hidden;background:var(--label-white)}
  .label .band{position:absolute;left:0;right:0;bottom:0;text-align:center}
  .logo{position:absolute;border-radius:50%;display:flex;align-items:center;justify-content:center;color:var(--white);font-weight:400;letter-spacing:.04em}
  .name{font-weight:700;letter-spacing:.18em;text-transform:uppercase}
  .volume{font-weight:500;letter-spacing:.08em}

  /* Rasieröl */
  .oil{left:114px;top:344px;width:344px;height:299px}
  .oil .logo{left:103px;top:23px;width:99px;height:99px;background:var(--orange);font-size:26px}
  .oil .band{height:131px;background:var(--yellow);color:var(--orange-text)}
  .oil .name{font-size:17px;margin-top:17px}
  .oil .scent{font-size:17px;font-weight:400;letter-spacing:.18em;margin-top:2px}
  .oil .volume{font-size:13px;margin-top:21px}

  /* After Shave */
  .balm{left:557px;top:505px;width:155px;height:218px}
  .balm .logo{left:36px;top:21px;width:82px;height:82px;background:var(--teal);font-size:21px}
  .balm .band{height:91px;background:var(--teal-band);color:var(--white)}
  .balm .name{font-size:12.5px;line-height:14px;margin-top:15px;letter-spacing:.16em}
  .balm .volume{font-size:13px;margin-top:12px;letter-spacing:.02em}

  /* Rasiercreme */
  .cream{left:813px;top:552px;width:270px;height:171px}
  .cream .logo{left:103px;top:13px;width:70px;height:70px;background:var(--green);font-size:18px}
  .cream .band{height:72px;background:var(--green-band);color:var(--green-text)}
  .cream .name{font-size:10.5px;margin-top:11px}
  .cream .volume{font-size:10px;margin-top:20px;color:var(--white);letter-spacing:.03em}

  /* Faltschachtel Rasierhobel */
  .panel{position:absolute;border:1px solid var(--line)}
  .flap{background:var(--flap);color:var(--white);text-align:center}
  .flap-top{left:711px;top:44px;width:358px;height:87px;transform:rotate(180deg);padding-top:12px;font-size:7px;line-height:10px}
  .flap-top .heading,.flap-bottom .heading{font-weight:700;letter-spacing:.04em;margin-bottom:4px}
  .flap-top .heading{font-size:7px}
  .front{left:711px;top:130px;width:358px;height:196px;background:var(--white);overflow:hidden}
  .front .logo{left:137px;top:32px;width:71px;height:71px;background:var(--sage);font-size:18px}
  .front .band{position:absolute;left:0;right:0;bottom:0;height:65px;background:var(--sage-band);text-align:center}
  .front .name{font-size:12px;color:var(--green-text);margin-top:25px;font-weight:600;letter-spacing:.22em}
  .badge{position:absolute;left:251px;top:92px;width:68px;height:68px;border-radius:50%;background:var(--white);border:1.5px solid var(--green)}
  .side{background:var(--white);top:130px;height:196px;width:87px}
  .side-left{left:625px}
  .side-left .logo{left:21px;top:72px;width:43px;height:43px;background:var(--sage);font-size:11px;transform:rotate(90deg)}
  .side-right{left:1068px}
  .flap-bottom{left:711px;top:325px;width:358px;height:87px;padding:16px 14px 0;font-size:7.2px;line-height:10px}
  .flap-bottom .heading{font-size:7.5px}
</style>
</head>
<body>

<section class="label oil">
  <div class="logo">flau</div>
  <div class="band">
    <p class="name">Rasieröl</p>
    <p class="scent">ORANGE</p>
    <p class="volume">30ml • 1.01 FL. OZ.</p>
  </div>
</section>

<section class="label balm">
  <div class="logo">flau</div>
  <div class="band">
    <p class="name">After Shave<br>Balsam</p>
    <p class="volume">60ml • 2.03 FL. OZ.</p>
  </div>
</section>

<section class="label cream">
  <div class="logo">flau</div>
  <div class="band">
    <p class="name">Rasiercreme</p>
    <p class="volume">60ml • 2.03 FL. OZ.</p>
  </div>
</section>

<section class="box">
  <div class="panel flap flap-top">
    <p class="heading">HERGESTELLT FÜR</p>
    <p>Torsten Kählbrink e.K. von tidewinders</p>
    <p>Holunderweg 27</p>
    <p>83047 Kolbenried</p>
    <p style="margin-top:3px;font-weight:600">www.flau.example</p>
  </div>
  <div class="panel side side-left"><div class="logo">flau</div></div>
  <div class="panel front">
    <div class="logo">flau</div>
    <div class="band"><p class="name">Rasierhobel</p></div>
    <div class="badge"></div>
  </div>
  <div class="panel side side-right"></div>
  <div class="panel flap flap-bottom">
    <p class="heading">INGREDIENTS:</p>
    <p>Aqua, Stearic Acid, Cocos Nucifera oil, Glycerin, Potassium Hydroxide, Litsea Cubeba oil, (and) Citrus Sinensis Peel oil, Orbignya Oleifera oil, Sodium Hydroxide, Macadamia ternifolia oil, Talc, Kaolin, Citric Acid, Simmondsia chinensis oil, Maris sal, C.I. 77892 (and) Rad Clay, Citral, Limonene, Linalool, Geraniol</p>
  </div>
</section>

</body>
</html>
```